Family Farm Business Requires Flyer for local CSA retail sales and local advertising

We need a flyer design for our small farm to help promote our CSA business. A CSA is when someone pre-pays for a summer's worth of produce, fruit, and eggs that are raised on our farm. They receive a weekly box of produce and essentially they buy a small share of the summer's bounty. We had a logo designed by someone here on sketch harbor so we would like the flyer to include the colors of the logo. The final design should reflect the different options for people the choose and then invite them to sign up to be a CSA Customer.

Target Market(s)

Busy families and moms who are limited in time to buy groceries or healthy food or produce. People who are passionate about local food and local produce.

Industry/Entity Type

Advertising

Font styles to use
Decorative
Script

Requirements
Must have
• Our logo, our farm information (website, social media, location) and contact info as well as the various options to choose from for our CSA farm share. I also included a picture of our business card so it would be good if it matched the colors/style of our card. Also the flyer will be printed on 8.5 x 11 paper and it will be double sided.

```html
<!DOCTYPE html>
<html lang="en">
<head>
<meta charset="utf-8">
<title>Nine Hollow Farm – CSA Shares</title>
<link rel="stylesheet" href="https://fonts.googleapis.com/css2?family=Raleway:wght@500;700&family=Yellowtail&display=swap">
<style>
:root{
  --leaf:#1b8f55;
  --tomato:#ea4a2c;
  --lime:#c6ef12;
  --lime-soft:#a9d94a;
  --pale:#eef3dc;
  --sun:#ffc21a;
  --sun-band:#fff200;
  --ink:#2b2b2b;
  --orange:#f47a20;
  --sky:#8fa9c8;
  --pine:#4f5d3a;
}
*{margin:0;padding:0;box-sizing:border-box}
html,body{width:851px;height:1200px;overflow:hidden;background:#fff}
.flyer{position:relative;width:851px;height:1200px;overflow:hidden;font-family:Arial,Helvetica,sans-serif;color:var(--ink)}
.hero-photo{position:absolute;left:0;top:0;width:851px;height:352px;
  background:linear-gradient(180deg,#c9d6e6 0%,var(--sky) 30%,#7c7f74 42%,var(--pine) 65%,#3e4a2d 100%)}
.farm-name{position:absolute;left:40px;top:70px;width:140px;font-family:Raleway,sans-serif;font-weight:700;
  font-size:34px;line-height:1.05;color:#fff;text-align:center;letter-spacing:2px}
.farm-name small{display:block;font-size:14px;letter-spacing:1px;margin-top:14px}
.tagline{position:absolute;left:210px;width:560px;top:262px;text-align:center;
  font-family:Yellowtail,cursive;font-size:70px;line-height:80px;color:var(--lime);white-space:nowrap}
.body-panel{position:absolute;left:0;top:352px;width:851px;height:680px;
  background:linear-gradient(90deg,var(--lime-soft) 0%,#cfe79a 50%,var(--pale) 100%)}
.headline{position:absolute;left:0;width:851px;text-align:center;font-family:Raleway,sans-serif;font-weight:700}
.headline.farm{top:360px;font-size:64px;color:var(--tomato)}
.headline.csa{top:436px;font-size:48px;color:var(--leaf);font-weight:500}
.intro{position:absolute;left:36px;top:518px;width:400px;list-style:none;font-size:15.5px;line-height:21px}
.intro li{position:relative;padding-left:22px}
.intro li::before,.payments li::before{content:"";position:absolute;left:0;top:4px;width:13px;height:13px;border-radius:50%;background:var(--leaf)}
.band{position:absolute;left:0;height:22px;padding-left:32px;font-size:15px;line-height:22px;color:var(--ink)}
.band.shares{top:654px;width:470px;background:var(--sun)}
.band.pay{top:820px;width:560px;background:var(--lime)}
.band.pickup{top:924px;width:690px;background:var(--sun-band)}
.options{position:absolute;left:36px;list-style:none;font-size:15.5px;line-height:21px}
.options li{position:relative;padding-left:14px}
.options li::before{content:"";position:absolute;left:0;top:6px;width:7px;height:7px;background:var(--orange)}
.options.shares-list{top:683px;width:345px}
.options.pickup-list{top:956px;width:640px}
.payments{position:absolute;left:36px;top:850px;list-style:none;font-size:15.5px;line-height:21px}
.payments li{position:relative;padding-left:22px}
.produce-art{position:absolute;left:470px;top:498px;width:370px;height:385px;border-radius:40px;
  background:radial-gradient(ellipse at 50% 55%,#e0533a 0%,#f0a940 35%,#8ab34a 60%,rgba(200,230,150,0) 75%)}
.box-art{position:absolute;left:620px;top:900px;width:220px;height:180px;border-radius:20px;
  background:radial-gradient(ellipse at 50% 45%,#5d9b3a 0%,#c49a6c 55%,rgba(230,240,200,0) 75%)}
.badge-art{position:absolute;border-radius:12px}
.badge-art.veg{left:716px;top:478px;width:104px;height:130px;background:var(--leaf);opacity:.8}
.badge-art.eggs{left:702px;top:716px;width:104px;height:130px;background:var(--sun)}
.badge-art.fresh{left:100px;top:1052px;width:104px;height:122px;background:var(--leaf)}
.badge-art.local{left:640px;top:1052px;width:106px;height:128px;background:var(--orange)}
.footer{position:absolute;left:0;top:1032px;width:851px;height:168px;background:var(--lime)}
.mail-to{position:absolute;left:230px;top:1047px;width:390px;text-align:center;font-size:13.5px;line-height:20px}
.phone{display:flex;justify-content:center;align-items:center;gap:8px;font-size:23px;font-weight:700;margin-top:2px;letter-spacing:1px}
</style>
</head>
<body>
<div class="flyer">
  <div class="hero-photo" role="img" aria-label="Photo of forested ridges beneath a mountain and blue sky"></div>
  <div class="farm-name">NINE HOLLOW FARM<small>MAPLE BEND, VA</small></div>
  <div class="tagline">Eat Fresh For Less</div>

  <div class="body-panel"></div>
  <h1 class="headline farm">Nine Hollow Farm</h1>
  <h2 class="headline csa">CSA shares available</h2>

  <ul class="intro">
    <li>This is the best way to get the freshest, tastiest and ecologically grown food on your family’s plate.</li>
    <li>The summer season runs from June 1st to October 11th for a total of 18 weeks.</li>
    <li>We grow a wide variety of popular fruits and vegetables and pastured eggs.</li>
  </ul>

  <div class="produce-art" role="img" aria-label="Illustration of a tipped bushel basket spilling vegetables and a basket of eggs"></div>
  <div class="badge-art veg" role="img" aria-label="Hand-lettered badge about home grown vegetables"></div>
  <div class="badge-art eggs" role="img" aria-label="Hand-lettered badge about free range eggs"></div>

  <div class="band shares">Share Options</div>
  <ul class="options shares-list">
    <li>Mini Share (1 to 2 people) <b>$325.00</b></li>
    <li>Standard Share ( 4 to 6 people) <b>$425.00</b></li>
    <li>Family Share $500.00 (6 to 8 people)</li>
    <li>Fruit Share Add-on <b>$50</b> to <b>$75</b> depending on size (please indicate when ordering)</li>
    <li>Egg Share Add-on <b>$90</b></li>
  </ul>

  <div class="band pay">Payment Options</div>
  <ul class="payments">
    <li>Check made payable to: Daniel Whitcombe / Nine Hollow Farm</li>
    <li>Debit/Credit Card/online transfer on website (coming soon!)</li>
    <li>Money Order (Daniel Whitcombe / Nine Hollow Farm)</li>
  </ul>

  <div class="band pickup">Preferred Pick Up Location for Summer CSA</div>
  <ul class="options pickup-list">
    <li>At Nine Hollow Farm on Thursdays (1820 Orchard Lane Maple Bend, VA 24099)</li>
    <li>Alder County Farmers Market on Saturdays (Circle One: Pre-Picked Market Shopper)</li>
    <li>Stonebrook Community Church Fairview on Thursday Afternoons</li>
  </ul>

  <div class="box-art" role="img" aria-label="Illustration of a cardboard box filled with fresh vegetables"></div>

  <div class="footer"></div>
  <div class="badge-art fresh" role="img" aria-label="Hand-lettered badge expressing love of farm fresh food"></div>
  <div class="mail-to">
    Please send to Completed Form and Check to:<br>
    Nine Hollow Farm<br>
    Daniel &amp; Marla Whitcombe<br>
    1820 Orchard Lane<br>
    Maple Bend, VA 24099
    <div class="phone">
      <svg width="24" height="24" viewBox="0 0 24 24" aria-hidden="true"><circle cx="12" cy="12" r="11" fill="none" stroke="var(--ink)" stroke-width="1.6"/><path d="M8 6.5c-1 1-1 3 1 6s4 5 6 5c1 0 1.6-.6 2-1.2l-2-2-1.4.8c-1-.5-2.7-2.2-3.2-3.2l.8-1.4-2-2Z" fill="var(--ink)"/></svg>
      (555) 013.4820
    </div>
  </div>
  <div class="badge-art local" role="img" aria-label="Hand-lettered badge expressing love of local food"></div>
</div>
</body>
</html>
```